PR & Jobs Workshop

We need a eye catching poster design (standard size) to attract people to register and attend a workshop. These will be posted in cafes, notice boards, grocery stores across the city.
Target Market(s)
Target audience is young people between 20-35 age.
Colors
Designer to choose colors to be used in the design.
Requirements
Must have
- (Main Heading)
- Free Jobs & PR Workshop
- (Body)
- What & Who
- - Where & how will I find jobs?
- - What jobs will lead to PR?
- - When & how can my family join me?
- - How much salary do I need?
- - I have a job, do I qualify for PR?
- - I don't have a job, do I qualify for PR?
- To get answers to all these questions, attend a FREE Jobs & PR Workshop by your Friendly & Frank Licensed Immigration Adviser, Tomas Reyland.
- License No: 738204915
- When & Where
- On Sunday, 30 September 2018
- 12-2 pm @ TBC
- TEXT "REGISTER" to 022 481 7390
- LIMITED SEATS ONLY
- (Add photo along with below text)
- Search for 'Tomas Reyland' on VidStream
- (Add logo along with below text)
- www.qmrworldwide.example
Nice to have
- Classy
Should not have
- Avoid too many colors

```html
<!DOCTYPE html>
<html lang="en">
<head>
<meta charset="utf-8">
<title>Jobs &amp; PR Free Workshop</title>
<link rel="stylesheet" href="https://fonts.googleapis.com/css2?family=Bebas+Neue&family=Oswald:wght@300;400&family=Montserrat:wght@400;600;700;800&display=swap">
<style>
  :root {
    --backdrop: #4a4a4a;
    --yellow: #fdbb1c;
    --yellow-deep: #eaa514;
    --orange: #f7861e;
    --ink: #1a1a1a;
    --white: #ffffff;
    --photo-grey: #cfcfcf;
  }
  * { margin: 0; padding: 0; box-sizing: border-box; }
  html, body { width: 960px; height: 1200px; overflow: hidden; background: var(--backdrop); }
  .poster {
    position: absolute; left: 84px; top: 38px;
    width: 793px; height: 1122px;
    background: var(--yellow); overflow: hidden;
    font-family: "Montserrat", sans-serif; color: var(--ink);
  }
  .abs { position: absolute; }
  .frame { left: 0; top: 0; }
  .headline {
    left: 0; width: 100%; text-align: center;
    font-family: "Bebas Neue", sans-serif; font-weight: 400;
    line-height: 1; white-space: nowrap; transform-origin: 50% 0;
  }
  .headline-top { top: 26px; font-size: 114px; }
  .headline-main { top: 122px; font-size: 111px; }
  .headline-main .light { color: var(--white); }
  .day { top: 220px; font-size: 66px; }
  .day .thin { font-family: "Oswald", sans-serif; font-weight: 300; font-size: 0.82em; text-transform: uppercase; }
  .date { top: 279px; font-size: 69px; color: var(--white); transform: scaleX(0.93); }
  .time { top: 337px; font-family: "Oswald", sans-serif; font-weight: 300; font-size: 59px; }
  .venue-1 { top: 397px; font-size: 40px; transform: scaleX(0.9); }
  .venue-2 { top: 435px; font-size: 39px; transform: scaleX(0.9); }
  .crowd-art {
    left: 428px; top: 434px; width: 365px; height: 440px;
    background: radial-gradient(ellipse 60% 55% at 60% 45%, rgba(224,158,20,0.75) 0%, rgba(234,165,20,0.45) 60%, rgba(253,187,28,0) 100%);
  }
  .section-title { left: 45px; top: 497px; font-size: 43px; font-weight: 800; line-height: 1; }
  .questions { left: 0; top: 547px; width: 540px; list-style: none; }
  .questions li {
    height: 42.7px; display: flex; align-items: center;
    padding-left: 70px; position: relative;
    font-size: 24px; font-weight: 800; white-space: nowrap;
  }
  .questions li::before {
    content: ""; position: absolute; left: 50px; top: 50%;
    width: 7px; height: 7px; margin-top: -3px; border-radius: 50%; background: var(--white);
  }
  .questions .lead { color: var(--white); }
  .questions li.band { background: linear-gradient(90deg, rgba(247,134,30,0) 0%, var(--orange) 10%, var(--orange) 72%, rgba(247,134,30,0) 100%); }
  .intro {
    left: 36px; top: 820px; width: 514px;
    font-size: 18.4px; line-height: 25.6px; text-align: justify; font-weight: 400;
  }
  .portrait {
    left: 608px; width: 166px; height: 166px;
    border: 3px solid var(--white);
    background: linear-gradient(180deg, #dcdcdc, var(--photo-grey));
  }
  .portrait-1 { top: 670px; }
  .portrait-2 { top: 886px; height: 164px; background: linear-gradient(180deg, #e4e4e4 0%, #a9a9a9 60%, #2a2a2a 100%); }
  .adviser-name { left: 596px; width: 190px; text-align: center; font-size: 16px; font-weight: 800; line-height: 18px; }
  .adviser-1 { top: 848px; }
  .contact-band { left: 0; top: 974px; width: 100%; height: 148px; background: var(--white); }
  .register-pill {
    left: 292px; top: 946px; width: 232px; height: 48px; border-radius: 10px;
    background: var(--ink); color: var(--white);
    display: flex; align-items: center; justify-content: center; gap: 8px;
    font-size: 29px; font-weight: 400;
  }
  .register-pill strong { color: var(--yellow); font-weight: 800; }
  .phone {
    left: 235px; top: 1001px; width: 340px; text-align: center;
    font-family: "Bebas Neue", sans-serif; font-size: 74px; line-height: 1;
    color: var(--yellow); white-space: nowrap;
  }
  .website { left: 230px; top: 1073px; width: 350px; text-align: center; font-size: 21px; line-height: 24px; font-weight: 600; white-space: nowrap; }
  .brand { left: 20px; top: 1024px; display: flex; align-items: center; gap: 10px; font-size: 22px; font-weight: 800; white-space: nowrap; }
  .brand-mark { width: 20px; height: 20px; background: var(--orange); }
  .channel { left: 596px; top: 1060px; width: 190px; text-align: center; }
  .channel-name { font-size: 16px; font-weight: 800; display: flex; align-items: center; justify-content: center; gap: 8px; }
  .channel-sub { font-size: 16px; font-weight: 600; display: flex; align-items: center; justify-content: center; gap: 10px; margin-top: 2px; }
  .channel-dot { width: 20px; height: 14px; border-radius: 3px; background: #e52d27; }
</style>
</head>
<body>
<div class="poster">
  <svg class="abs frame" width="793" height="1122" aria-hidden="true">
    <g stroke="#ffffff" stroke-width="2.5" fill="none">
      <polyline points="206,99 48,99 48,435 114,435"/>
      <polyline points="582,99 746,99 746,435 694,435"/>
    </g>
  </svg>

  <div class="abs crowd-art" role="img" aria-label="Faded silhouettes of business professionals standing together"></div>

  <h1 class="abs headline headline-top">Jobs &amp; PR</h1>
  <div class="abs headline headline-main">Free <span class="light">Workshop</span></div>
  <div class="abs headline day"><span class="thin">On</span> Sunday</div>
  <div class="abs headline date">7th and 14th October&nbsp; 2018</div>
  <div class="abs headline time">5-7 PM</div>
  <div class="abs headline venue-1">Harbourline Centre, Kowhai Community Hall</div>
  <div class="abs headline venue-2">14 Wexley Pl, Auckland CBD.</div>

  <h2 class="abs section-title">What &amp; Who</h2>
  <ul class="abs questions">
    <li><span><b class="lead">What jobs</b> will lead to PR?</span></li>
    <li class="band"><span><b class="lead">How much</b> salary do I need?</span></li>
    <li><span><b class="lead">Where &amp; how</b> will I find jobs?</span></li>
    <li class="band"><span><b class="lead">I have a job,</b> do I qualify for PR?</span></li>
    <li><span><b class="lead">When &amp; how</b> can my family join me?</span></li>
    <li class="band"><span><b class="lead">I don't have a job,</b> do I qualify for PR?</span></li>
  </ul>

  <p class="abs intro">To get answers to all these questions, attend any of these workshops by your Friendly and Frank Licensed Immigration Advisers, Marlene Voskuijl (License No: 614093827) &amp; Tomas Reyland (License No: 738204915).</p>

  <div class="abs portrait portrait-1" role="img" aria-label="Placeholder portrait of adviser Marlene Voskuijl"></div>
  <div class="abs adviser-name adviser-1">MARLENE VOSKUIJL</div>

  <div class="abs contact-band"></div>
  <div class="abs portrait portrait-2" role="img" aria-label="Portrait photo of adviser Tomas Reyland in a dark suit"></div>

  <div class="abs register-pill"><strong>REGISTER</strong> to</div>
  <div class="abs phone">022 481 7390</div>
  <div class="abs website">www.qmrworldwide.example</div>

  <div class="abs brand"><span class="brand-mark"></span>QMR Worldwide</div>

  <div class="abs channel">
    <div class="channel-name">TOMAS REYLAND
      <svg width="20" height="20" viewBox="0 0 20 20" aria-hidden="true"><circle cx="8" cy="8" r="5.5" fill="none" stroke="#f7861e" stroke-width="2.2"/><line x1="12" y1="12" x2="17.5" y2="17.5" stroke="#f7861e" stroke-width="2.6" stroke-linecap="round"/></svg>
    </div>
    <div class="channel-sub">on VidStream <span class="channel-dot"></span></div>
  </div>
</div>
</body>
</html>
```